依頼詳細
法人向け新サービスのダイレクトメール(はがきサイズ)を制作しますので、オフセット印刷入稿用デザインをお願い致します。

表は宛名印刷用ですので、下4分の一程度のデザイン(単色1c)、裏は全面デザイン(4c)をお願いします。

アウトドア用品の会社ですが、今回は法人向けDMですので、目を引くデザインを求めます。

・テンプレート(win・mac)用添付いたします。
・テキストは添付のとおりですが、デザイン・文字級数含め、レイアウトなどは、自由にご提案ください。
・写真画像は添付しますが、カンプ用のダミーですので、発注者が決まり次第、本番用の写真をお渡しします。
記載項目
テキストは添付ファイルの通りです。
希望イメージ
シンプル 複雑
単色 カラフル
暗い 明るい
日常 高級
遊び心 厳粛
未来的 伝統的
女性的 男性的
希望する色
水色系、茶系、緑系、黄・オレンジ系、色味などは弊社HPなども参考にしてください。さわやかな青系なども可です。
納品ファイル
• 高解像度JPG (.jpg)
• イラストレーター形式 (.ai)
補足説明
■ 選んだ理由

法人向けという堅い部分とアウトドア用品という柔らかさのバランス、見出しや文字級数の強弱のつけ方、DMという特性上、ぱっと見で入ってくる印象などで決定させていただきました。

■ 提案者全員のお礼・コメント

沢山のご提案ありがとうございました。
皆様それぞれに良い部分がありましたが、上記の部分を踏まえて、決定させていただきました。
またご機会がありましたら、何卒宜しくお願い申し上げます。

```html
<!DOCTYPE html>
<html lang="ja">
<head>
<meta charset="utf-8">
<title>あおぞらや ポストカード 表面</title>
<link rel="stylesheet" href="https://fonts.googleapis.com/css2?family=Noto+Sans+JP:wght@400;700;900&family=Roboto+Condensed:wght@400;700&display=swap">
<style>
  :root {
    --ink: #111111;
    --paper: #ffffff;
    --tab-grey: #8a8a8a;
    --rule: #222222;
  }
  html, body {
    margin: 0;
    padding: 0;
    overflow: hidden;
    background: var(--paper);
  }
  .postcard {
    position: relative;
    width: 818px;
    height: 1200px;
    background: var(--paper);
    color: var(--ink);
    font-family: "Noto Sans JP", sans-serif;
    overflow: hidden;
  }
  .postcard-label {
    position: absolute;
    top: 36px;
    left: 0;
    width: 100%;
    text-align: center;
    font-family: "Roboto Condensed", sans-serif;
    font-weight: 700;
    font-size: 19px;
    letter-spacing: 2px;
  }
  .zip-boxes {
    position: absolute;
    top: 92px;
    left: 402px;
  }
  .brand-block {
    position: absolute;
    top: 958px;
    left: 0;
    width: 100%;
    text-align: center;
  }
  .brand-tagline {
    font-weight: 900;
    font-size: 25px;
    letter-spacing: 1px;
    line-height: 1;
  }
  .brand-name {
    margin-top: 10px;
    font-weight: 900;
    font-size: 54px;
    letter-spacing: 2px;
    line-height: 1;
  }
  .contact-tab {
    position: absolute;
    top: 1058px;
    left: 33px;
    width: 240px;
    height: 25px;
    background: var(--tab-grey);
    color: var(--paper);
    font-weight: 700;
    font-size: 15px;
    line-height: 25px;
    text-align: center;
    clip-path: polygon(0 0, 94% 0, 100% 100%, 0 100%);
  }
  .contact-rule {
    position: absolute;
    top: 1083px;
    left: 33px;
    width: 752px;
    height: 3px;
    background: var(--rule);
  }
  .contact-line {
    position: absolute;
    top: 1092px;
    left: 33px;
    width: 752px;
    display: flex;
    align-items: baseline;
    font-family: "Roboto Condensed", sans-serif;
    font-weight: 700;
    line-height: 1;
    white-space: nowrap;
  }
  .contact-tel {
    font-size: 40px;
  }
  .contact-tel .tel-prefix {
    font-size: 30px;
  }
  .contact-mail {
    margin-left: 8px;
    font-size: 17px;
  }
  .contact-web {
    margin-left: auto;
    font-size: 22px;
  }
  .contact-address {
    position: absolute;
    top: 1138px;
    left: 33px;
    font-size: 16px;
    font-weight: 400;
    line-height: 1;
  }
  .search-box {
    position: absolute;
    top: 1131px;
    left: 560px;
    width: 225px;
    height: 28px;
    display: flex;
    border: 2px solid var(--ink);
    box-sizing: border-box;
    font-size: 14px;
  }
  .search-field {
    flex: 1;
    padding-left: 8px;
    line-height: 24px;
  }
  .search-button {
    width: 60px;
    border-left: 2px solid var(--ink);
    text-align: center;
    line-height: 24px;
    font-weight: 700;
  }
</style>
</head>
<body>
  <main class="postcard">
    <div class="postcard-label">POST CARD</div>

    <svg class="zip-boxes" width="364" height="66" viewBox="0 0 364 66" aria-label="郵便番号欄">
      <g fill="none" stroke="var(--ink)" stroke-width="4">
        <rect x="2" y="2" width="44" height="62"/>
        <rect x="54" y="2" width="44" height="62"/>
        <rect x="106" y="2" width="44" height="62"/>
      </g>
      <g fill="none" stroke="var(--ink)" stroke-width="1.6">
        <rect x="162" y="3" width="44" height="60"/>
        <rect x="212" y="3" width="44" height="60"/>
        <rect x="262" y="3" width="44" height="60"/>
        <rect x="312" y="3" width="44" height="60"/>
      </g>
    </svg>

    <section class="brand-block">
      <div class="brand-tagline">遊びかた総合提案</div>
      <div class="brand-name">あおぞらや</div>
    </section>

    <div class="contact-tab">お問い合わせはお気軽に!</div>
    <div class="contact-rule"></div>

    <div class="contact-line">
      <span class="contact-tel"><span class="tel-prefix">tel.</span>0555-00-1234</span>
      <span class="contact-mail">info@aozoraya.example</span>
      <span class="contact-web">www.aozoraya.example</span>
    </div>
    <div class="contact-address">〒400-0000 山梨県甲府市中央 1-2-3</div>

    <div class="search-box">
      <div class="search-field">あおぞらや</div>
      <div class="search-button">検索</div>
    </div>
  </main>
</body>
</html>
```